Business Card Design

I need a business card for a new company based in Australia called "ClinoPath".

Its a cloud program for GPs that allows them to search for the specialist they require using a simple user friendly tool.

I would like the colours to match those in the program (the colours in the logo attached).

The final design should reflect the programs clarity, ease of use and professionalism.

Target Market(s)

GPs and other Health Professionals

Industry/Entity Type

Business

Contact Information for Business Card

ClinoPath; The Whole Consultant Index; Maren Tolhurst CEO; 0417385261; maren@clinopath.example; www.clinopath.example

Requirements
Must have
• Must have the logo attached; the web address and my name and phone number
Nice to have
• the slogan "The Whole Consultant Index"

```html
<!DOCTYPE html>
<html lang="en">
<head>
<meta charset="utf-8">
<title>ClinoPath Business Card</title>
<link rel="stylesheet" href="https://fonts.googleapis.com/css2?family=Questrial&family=Open+Sans:wght@400;600;700&display=swap">
<style>
  :root {
    --brand-cyan: #19aee0;
    --brand-grey: #8c8c8c;
    --swoosh-grey: #9a9a9c;
    --ink: #2b2b2b;
    --card-white: #ffffff;
    --page-bg: #ecebe8;
  }
  * { box-sizing: border-box; }
  html, body {
    margin: 0;
    width: 1200px;
    height: 1200px;
    overflow: hidden;
    background: var(--page-bg);
  }
  .canvas {
    position: relative;
    width: 1200px;
    height: 1200px;
  }
  .card {
    position: absolute;
    left: 160px;
    width: 880px;
    height: 500px;
    background: var(--card-white);
    border-radius: 30px;
    overflow: hidden;
    box-shadow: 0 6px 20px rgba(0,0,0,0.12);
  }
  .card--front { top: 70px; }
  .card--back { top: 630px; }

  .wordmark {
    font-family: "Questrial", sans-serif;
    color: var(--brand-cyan);
    line-height: 1;
    letter-spacing: -2px;
    margin: 0;
    font-weight: 400;
  }
  .tagline {
    font-family: "Questrial", sans-serif;
    color: var(--brand-grey);
    margin: 0;
    line-height: 1;
  }

  /* Front */
  .card--front .brand {
    position: absolute;
    left: 78px;
    top: 62px;
  }
  .card--front .wordmark { font-size: 100px; }
  .card--front .tagline { font-size: 33px; margin-top: 6px; letter-spacing: 0.3px; }

  .person {
    position: absolute;
    right: 510px;
    top: 232px;
    text-align: right;
    font-family: "Open Sans", sans-serif;
  }
  .person__name {
    margin: 0;
    font-size: 29px;
    font-weight: 700;
    color: var(--brand-cyan);
    line-height: 1.2;
  }
  .person__role {
    margin: 4px 0 0;
    font-size: 22px;
    color: var(--brand-grey);
  }
  .divider {
    position: absolute;
    left: 392px;
    top: 222px;
    width: 2px;
    height: 92px;
    background: #d6d6d6;
  }
  .contact {
    position: absolute;
    left: 414px;
    top: 222px;
    margin: 0;
    padding: 0;
    list-style: none;
    font-family: "Open Sans", sans-serif;
    font-size: 27px;
    color: var(--ink);
  }
  .contact__item {
    display: flex;
    align-items: center;
    gap: 12px;
    height: 44px;
  }
  .contact__icon { width: 24px; height: 24px; flex: none; }

  .wave {
    position: absolute;
    left: 0;
    bottom: 0;
    width: 880px;
    height: 200px;
  }
  .card--front .web {
    position: absolute;
    right: 40px;
    bottom: 44px;
    margin: 0;
    font-family: "Open Sans", sans-serif;
    font-size: 26px;
    line-height: 1.2;
    letter-spacing: 2px;
    color: var(--card-white);
  }

  /* Back */
  .card--back .brand {
    position: absolute;
    left: 0;
    right: 0;
    top: 118px;
    text-align: center;
  }
  .card--back .wordmark { font-size: 116px; }
  .card--back .tagline { font-size: 37px; margin-top: 8px; }
  .card--back .web {
    position: absolute;
    left: 0;
    right: 0;
    top: 338px;
    margin: 0;
    text-align: center;
    font-family: "Open Sans", sans-serif;
    font-size: 34px;
    letter-spacing: 3.5px;
    color: var(--ink);
  }
</style>
</head>
<body>
<main class="canvas">

  <section class="card card--front" aria-label="Business card front">
    <div class="brand">
      <p class="wordmark">ClinoPath</p>
      <p class="tagline">The Whole Consultant Index</p>
    </div>

    <div class="person">
      <p class="person__name">Maren Tolhurst</p>
      <p class="person__role">CEO</p>
    </div>
    <div class="divider"></div>

    <ul class="contact">
      <li class="contact__item">
        <svg class="contact__icon" viewBox="0 0 24 24" aria-hidden="true">
          <circle cx="12" cy="12" r="11" fill="none" stroke="var(--brand-cyan)" stroke-width="2"/>
          <path d="M8.5 6.5c-1 1-1.2 3 .6 6s4 4.6 5.6 4.6c.8 0 1.5-.6 1.8-1.2l-2-2-1.3.8c-1-.5-2.4-2-3-3.3l.9-1.2-1.7-2.2z" fill="var(--brand-cyan)"/>
        </svg>
        <span>0417385261</span>
      </li>
      <li class="contact__item">
        <svg class="contact__icon" viewBox="0 0 24 24" aria-hidden="true">
          <rect x="2" y="6" width="20" height="14" rx="2" fill="var(--brand-cyan)"/>
          <path d="M3 7l9 7 9-7" fill="none" stroke="#fff" stroke-width="1.8"/>
        </svg>
        <span>maren@clinopath.example</span>
      </li>
    </ul>

    <svg class="wave" viewBox="0 0 880 200" preserveAspectRatio="none" aria-hidden="true">
      <path d="M0 200 L0 168 C150 166 260 140 360 80 C300 140 240 180 200 200 Z" fill="var(--swoosh-grey)"/>
      <path d="M230 200 C330 120 520 60 880 50 L880 200 Z" fill="var(--brand-cyan)"/>
      <path d="M0 124 C230 112 430 22 880 22" fill="none" stroke="var(--brand-cyan)" stroke-width="5"/>
    </svg>
    <p class="web">www.clinopath.example</p>
  </section>

  <section class="card card--back" aria-label="Business card back">
    <div class="brand">
      <p class="wordmark">ClinoPath</p>
      <p class="tagline">The Whole Consultant Index</p>
    </div>
    <p class="web">www.clinopath.example</p>
  </section>

</main>
</body>
</html>
```